Heritage Hollow Business Cards

Require a business card design. <br/><br/>Needs to include logo (either round or long version) plus these details:<br/>Maya Torvel<br/>Heritage Hollow<br/>maya@quonbrook.com.au<br/>02 6481 7390<br/>PO Box Glenwarra NSW 2913<br/>www.heritagehollow.com.au<br/><br/>I need in an editable format so that I can create for multiple staff members. <br/><br/>

Target Market(s)

We are an online store selling renovation products to home owners are builders. Looking for a classic classy design.

Industry/Entity Type

Home And Garden

Contact Information for Business Card

Maya Torvel
Heritage Hollow
maya@quonbrook.com.au
02 6481 7390
PO Box Glenwarra NSW 2913
www.heritagehollow.com.au

Colors

Designer to choose colors to be used in the design.

Requirements
Must have
• Must include Logo.

```html
<!DOCTYPE html>
<html lang="en">
<head>
<meta charset="utf-8">
<title>Heritage Hollow Business Cards</title>
<link href="https://fonts.googleapis.com/css2?family=Carlito:wght@400;700&display=swap" rel="stylesheet">
<style>
  :root {
    --sage: #516f60;
    --paper: #ffffff;
    --backdrop: #e6e7e6;
    --ink-light: #ffffff;
  }
  * { margin: 0; padding: 0; box-sizing: border-box; }
  html, body {
    width: 1200px;
    height: 915px;
    overflow: hidden;
    background: var(--backdrop);
    font-family: "Carlito", "Calibri", sans-serif;
  }
  .card {
    position: absolute;
    left: 305px;
    width: 589px;
    height: 337px;
  }
  .card-front {
    top: 76px;
    background: var(--paper);
  }
  .brand-mark {
    position: absolute;
    left: 30px;
    top: 118px;
    width: 130px;
    height: 130px;
  }
  .brand-name {
    position: absolute;
    left: 50px;
    top: 255px;
    font-size: 56px;
    font-weight: 400;
    line-height: 1;
    color: var(--sage);
    letter-spacing: 0.5px;
    white-space: nowrap;
  }
  .front-band {
    position: absolute;
    left: 0;
    bottom: 0;
    width: 100%;
    height: 17px;
    background: var(--sage);
  }
  .card-back {
    top: 501px;
    background: var(--sage);
    color: var(--ink-light);
  }
  .staff-name {
    position: absolute;
    left: 166px;
    top: 101px;
    font-size: 20px;
    font-weight: 400;
  }
  .staff-name .surname { font-weight: 700; }
  .contact-list {
    position: absolute;
    left: 166px;
    top: 157px;
    list-style: none;
    font-size: 16px;
    line-height: 23.5px;
  }
</style>
</head>
<body>
  <section class="card card-front">
    <svg class="brand-mark" viewBox="0 0 130 130" aria-hidden="true">
      <circle cx="65" cy="65" r="63" fill="none" stroke="var(--sage)" stroke-width="1.5"/>
    </svg>
    <div class="brand-name">Heritage Hollow</div>
    <div class="front-band"></div>
  </section>

  <section class="card card-back">
    <p class="staff-name">Maya <span class="surname">TORVEL</span></p>
    <ul class="contact-list">
      <li class="contact-phone">02 6481 7390</li>
      <li class="contact-address">PO Box Glenwarra NSW 2913</li>
      <li class="contact-email">maya@quonbrook.com.au</li>
    </ul>
  </section>
</body>
</html>
```